UK Loan Company wanting to send a Christmas themed flyer to closed customers offering credit.

We need an A5 design. We want to invite closed customers back to our business by providing a flyer which contains a blank box where we can print how much credit we can offer. (We will add the amount ourselves)

Any customers who reopen their account has chance to win a laptop!

See attached word document for further information

Target Market(s)

UK home credit

Font styles to use
Serif
Sans Serif

Colors

Designer to choose colors to be used in the design.

Requirements
Must have
• our company logo see www.maplecrestfin.co.uk
• Seasons Greetings Title (see attached word draft)
• Credit Blank Box
• Representative example
• Authorised and regulated by The Marsden Standards Board
Nice to have
• Vouchtree logo and store outlets?

```html
<!DOCTYPE html>
<html lang="en">
<head>
<meta charset="utf-8">
<title>Season's Greetings – Maplecrest Finance</title>
<link rel="stylesheet" href="https://fonts.googleapis.com/css2?family=Yellowtail&family=Fira+Sans+Extra+Condensed:wght@600;700&family=Open+Sans:wght@600&family=Lato:wght@400;700&family=Montserrat:wght@600;700&display=block">
<style>
  :root {
    --flame: #f45b22;
    --amber: #f7941d;
    --sun: #f7c520;
    --lemon: #f5e53f;
    --gold-text: #f5d000;
    --paper: #ffffff;
    --cream-box: #fde6a2;
    --peach-block: #fdb45a;
    --taupe: #9b8b7c;
    --ink: #1d1d1d;
  }
  html, body {
    margin: 0;
    padding: 0;
    overflow: hidden;
    background: var(--paper);
  }
  .flyer {
    position: relative;
    width: 846px;
    height: 1200px;
    overflow: hidden;
    background: var(--flame);
  }
  .backdrop {
    position: absolute;
    inset: 0;
  }
  .greeting-title {
    position: absolute;
    left: 50px;
    top: 48px;
    margin: 0;
    font-family: "Yellowtail", cursive;
    font-weight: 400;
    font-size: 112px;
    line-height: 126px;
    color: var(--lemon);
  }
  .greeting-title span { display: block; }
  .greeting-title .line-two { margin-left: 4px; }
  .invitation {
    position: absolute;
    left: 77px;
    top: 346px;
    margin: 0;
    font-family: "Fira Sans Extra Condensed", sans-serif;
    font-weight: 700;
    font-size: 39px;
    line-height: 48px;
    color: var(--gold-text);
    text-shadow: 1px 2px 2px rgba(90, 60, 0, 0.45);
    white-space: nowrap;
  }
  .credit-box {
    position: absolute;
    left: 71px;
    top: 500px;
    width: 758px;
    height: 221px;
    background: var(--cream-box);
  }
  .credit-accent {
    position: absolute;
    left: 38px;
    top: 551px;
    width: 164px;
    height: 148px;
    background: var(--peach-block);
  }
  .credit-offer {
    position: absolute;
    left: 85px;
    top: 508px;
    margin: 0;
    font-family: "Open Sans", sans-serif;
    font-weight: 600;
    font-size: 31px;
    line-height: 38px;
    letter-spacing: -0.6px;
    color: var(--taupe);
    transform: scaleX(0.88);
    transform-origin: left top;
    white-space: nowrap;
  }
  .rep-example {
    position: absolute;
    left: 85px;
    top: 735px;
    margin: 0;
    font-family: "Lato", sans-serif;
    font-size: 18px;
    line-height: 24px;
    color: var(--ink);
    white-space: nowrap;
  }
  .rep-example strong { font-weight: 700; }
  .terms {
    position: absolute;
    left: 85px;
    top: 874px;
    margin: 0;
    font-family: "Lato", sans-serif;
    font-size: 18px;
    line-height: 24px;
    color: var(--ink);
    white-space: nowrap;
  }
  .prize-draw {
    position: absolute;
    left: 85px;
    top: 945px;
    margin: 0;
    font-family: "Montserrat", sans-serif;
    font-weight: 700;
    font-size: 21px;
    line-height: 29px;
    letter-spacing: 0.8px;
    color: var(--ink);
    white-space: nowrap;
  }
  .contact {
    position: absolute;
    left: 84px;
    top: 1064px;
    margin: 0;
    font-family: "Montserrat", sans-serif;
    font-weight: 700;
    font-size: 17px;
    letter-spacing: 1.3px;
    color: var(--paper);
    white-space: nowrap;
  }
  .contact .phone {
    font-size: 30px;
    letter-spacing: 2px;
    margin-left: 10px;
  }
  .regulatory {
    position: absolute;
    left: 0;
    right: 0;
    top: 1136px;
    margin: 0;
    text-align: center;
    font-family: "Fira Sans Extra Condensed", sans-serif;
    font-weight: 600;
    font-size: 16px;
    line-height: 22px;
    color: var(--lemon);
  }
</style>
</head>
<body>
<main class="flyer">
  <svg class="backdrop" width="846" height="1200" viewBox="0 0 846 1200" aria-hidden="true">
    <defs>
      <radialGradient id="globe-glow" cx="45%" cy="45%" r="60%">
        <stop offset="0%" stop-color="#f2d27a"/>
        <stop offset="45%" stop-color="#d9a21c"/>
        <stop offset="80%" stop-color="#a8641a"/>
        <stop offset="100%" stop-color="#8a2a18"/>
      </radialGradient>
    </defs>
    <rect width="846" height="1200" fill="var(--flame)"/>
    <path d="M0,251 C250,200 600,120 846,80 V131 C600,170 250,260 0,314Z" fill="var(--amber)"/>
    <path d="M0,314 C250,260 600,170 846,131 V283 C600,290 250,340 0,397Z" fill="var(--sun)"/>
    <path d="M0,397 C250,340 600,290 846,283 V1200 H0Z" fill="var(--paper)"/>
    <path d="M0,960 C150,990 300,1060 420,1040 C560,1010 640,840 720,826 C780,816 820,830 846,845 V1200 H0Z" fill="var(--sun)"/>
    <path d="M0,1000 C150,1040 300,1090 440,1070 C580,1050 660,900 740,890 C800,885 830,900 846,910 V1200 H0Z" fill="var(--amber)"/>
    <path d="M0,1060 C120,1090 280,1110 420,1095 C570,1080 660,960 760,950 C810,946 835,955 846,960 V1200 H0Z" fill="var(--flame)"/>
    <path d="M0,1095 C200,1070 420,1060 846,1095 V1112 C420,1080 200,1090 0,1112Z" fill="var(--sun)"/>
  </svg>
  <svg class="backdrop" width="846" height="1200" viewBox="0 0 846 1200" role="img" aria-label="Photo of a Santa snow globe on a red gift sack">
    <circle cx="552" cy="157" r="233" fill="url(#globe-glow)"/>
  </svg>

  <h1 class="greeting-title"><span>Season's</span><span class="line-two">Greetings</span></h1>

  <p class="invitation">As a valued previous customer, we would like<br>to invite you to reopen your account and<br>have a chance to win a Laptop.</p>

  <div class="credit-box"></div>
  <div class="credit-accent"></div>
  <p class="credit-offer">Treat yourself with one of our<br>cash loans or Vouchtree vouchers<br>which would make an ideal gift.<br>We would be delighted to offer<br>credit of up to</p>

  <p class="rep-example"><strong>Representative example:</strong><br>
    Loan amount £150.00 payable over 22 weeks at £10.50 per week.<br>
    Interest is £81.00.<br>
    The Total amount payable is £231.00.<br>
    Interest rate is 127.99% per annum (fixed). 716.47% APR representative</p>

  <p class="terms">Terms and conditions apply.<br>
    All credit is subject to status &amp; affordability. Written quotations on request</p>

  <p class="prize-draw">All customers that reopen their accounts with us<br>
    before the 18th December 2019 will be entered into<br>
    our free prize with the chance to win a 17” Brevlan Laptop.</p>

  <p class="contact">For more information contact our office on <span class="phone">01632 960 418</span></p>

  <p class="regulatory">Authorised and regulated by The Marsden Standards Board. Contact address: Maplecrest Finance (Yorkshire) Ltd,<br>
    Harbour House, Elmfield Business Park, Kestrel Way, Northby NB4 7QT. Registered in England No 5182736</p>
</main>
</body>
</html>
```